依頼詳細
犬と一緒にアウトドアを楽しめる商品の企画・製造・販売を手掛けます。
先日当サイトで募集したロゴが確定しましたので、そちらを用いた名刺のデザイン案をお寄せください。名刺は2、3色以内で活版印刷を予定しています(単色も可)ので、グラデーションなどを使用しないデザインをお願いいたします。
記載項目
以下の項目が含まれていれば、レイアウトなども含め特に制限はありません。
表面は「屋号」「役職」「氏名」「氏名ローマ字」「郵便番号」「所在地1」「所在地2」「電話番号」「メールアドレス」「URL」
裏面は「ロゴ」キャラだけ文字だけでも可
希望イメージ
シンプル 複雑
単色 カラフル
暗い 明るい
日常 高級
遊び心 厳粛
未来的 伝統的
女性的 男性的
希望する色
納品ファイル
• 高解像度JPG (.jpg)
• イラストレーター形式 (.ai)
• PNG形式 (.png)
補足説明
ブランド名
PIREL(ぴれる)※屋号ではない
所在地について
「所在地1:都道府県市区町村番地」「所在地2:建物名フロア」となります。
例)
〒1234567
所在地1県所在地1市所在地1区所在地1-2-3
所在地2ビル所在地2階

活版印刷での名刺を想定しておりましたので割とシンプルなデザインの提案が多い中、
ブランド特性に配慮いただき遊び心を取り入れていただいたところがポイントと
なりました。

事業が動き出したばかりということもあり、今後もご協力をいただく機会があるかと
思いますので、その節はまた提案いただけると助かります。

```html
<!DOCTYPE html>
<html lang="ja">
<head>
<meta charset="utf-8">
<title>名刺 表面 — PIREL</title>
<link rel="stylesheet" href="https://fonts.googleapis.com/css2?family=Noto+Sans+JP:wght@400;500&display=swap">
<style>
  :root {
    --stage: #e9e9e9;
    --paper: #ffffff;
    --brand-orange: #f39519;
    --paw-tint: #fbd9ad;
    --ink: #1a1a1a;
    --on-brand: #ffffff;
  }
  html, body {
    margin: 0;
    width: 810px;
    height: 1200px;
    overflow: hidden;
    background: var(--stage);
    font-family: "Noto Sans JP", sans-serif;
    color: var(--ink);
  }
  .business-card {
    position: absolute;
    left: 48px;
    top: 10px;
    width: 714px;
    height: 1180px;
    background: var(--paper);
  }
  .brand-band {
    position: absolute;
    top: 0;
    right: 0;
    width: 150px;
    height: 100%;
    background: var(--brand-orange);
  }
  .brand-mark {
    position: absolute;
    left: 35px;
    top: 100px;
    width: 80px;
    height: 80px;
    border-radius: 50%;
    background: var(--on-brand);
  }
  .brand-name {
    position: absolute;
    left: 38px;
    top: 240px;
    writing-mode: vertical-rl;
    font-size: 70px;
    font-weight: 500;
    letter-spacing: 6px;
    line-height: 1;
    color: var(--on-brand);
  }
  .person {
    position: absolute;
    left: 44px;
    top: 136px;
  }
  .person__title {
    font-size: 22px;
    letter-spacing: 6px;
    margin: 0 0 8px;
  }
  .person__name {
    font-size: 56px;
    font-weight: 500;
    letter-spacing: 4px;
    line-height: 1.1;
    margin: 0;
  }
  .person__name-roman {
    font-size: 25px;
    margin: 10px 0 0;
  }
  .paw-trail {
    position: absolute;
    left: 143px;
    top: 510px;
    width: 346px;
    height: 300px;
    background: var(--paw-tint);
  }
  .company {
    position: absolute;
    left: 44px;
    top: 842px;
    font-size: 25px;
    line-height: 46px;
  }
  .company__trade-name {
    font-weight: 500;
    margin: 0 0 4px;
  }
  .company__lines {
    margin: 0;
    padding: 0;
    list-style: none;
    font-size: 24px;
  }
</style>
</head>
<body>
  <article class="business-card">
    <section class="person">
      <p class="person__title">役職</p>
      <h1 class="person__name">名刺　一郎</h1>
      <p class="person__name-roman">Ichiro Meishi</p>
    </section>

    <div class="paw-trail" role="img" aria-label="斜めに続く犬の足跡のイラスト"></div>

    <section class="company">
      <p class="company__trade-name">屋号名</p>
      <ul class="company__lines">
        <li>〒123-4567</li>
        <li>所在地1県所在地1市所在地1区</li>
        <li>所在地1−2−3　所在地2ビル所在地2階</li>
        <li>TEL.000-000-0000</li>
        <li>E-mail　□□□□□□@□□□□□□</li>
        <li>http://www.□□□□□□□□</li>
      </ul>
    </section>

    <aside class="brand-band">
      <span class="brand-mark" aria-hidden="true"></span>
      <span class="brand-name">PIREL</span>
    </aside>
  </article>
</body>
</html>
```